Flyer für eine Immobilienverwaltung
Zielgruppe
ich bitte die Dienste einer Immobilienverwaltung an sowie die Versicherungen und Finanzierungen dieser (siehe auch dem angehängten Flyer)
Zielgruppe sind Investoren, Eigentümer (keine WEG Verwaltung) die einen Rundum Service möchten.
Aufgabenstellung
Unser Konzept: Wenige Objekte, Intensive Betreuung
Unser Fokus: Ertrag & Entwicklung
Unsere Vision ist es, durch intensive, ganzheitliche Betreuung und strategisches Life-Cycle-Management die nachhaltige Ertragsstärke Ihrer Liegenschaft zu sichern und ihren Wert zukunftsweisend zu steigern.
Zusätzlich sollen hervorgehoben werden das es ein Rundumservice von vor Vertragsabschluss bis zum Sanierungs und Renovierungsmanagement geht.
Ich habe den Inhalt des Flyers beigefügt (gerne noch Änderungen oder Vorschläge)
Ebenfalls würde ich gerne ein Bild haben, welches dem angehängten sehr ähnelt.
Update
Leider habe ich noch kein Logo. ich würde gerne eins haben mit einem ähnlichen Bild wie ich angehängt habe, in dem man die Immobilien sieht, zusammen mit dem Namen: Haven Crest Property Stewardship. Farbwahl bin ich offen. Es ist aufgefallen, dass die Kontaktdaten fehlen. Diese sind hier.
Jonas Trewelt
Info@wohnwerk-jt.de
Mobil: +49 1573 42 19 605
Am Lindenhang 7, 73453 Abtsgmünd
Update:
Ich habe noch Bild von mir angefügt, das zu den Kontaktdaten kommen soll.

```html
<!DOCTYPE html>
<html lang="de">
<head>
<meta charset="utf-8">
<title>Haven Crest Property Stewardship – Flyer</title>
<link href="https://fonts.googleapis.com/css2?family=Montserrat:ital,wght@0,400;0,600;0,700;0,800;1,400;1,800&family=Source+Sans+3:wght@400;600;700&display=swap" rel="stylesheet">
<style>
:root{
  --navy:#1d3f7a;
  --teal:#2a6b73;
  --ink:#222;
  --sky-light:#eef6fa;
  --sky-mid:#bfe0ee;
  --glass:#3f9cc4;
  --glass-deep:#0d3f66;
  --paper:#ffffff;
  --stage:#d6d6d3;
  --rule:#b9d3d6;
}
*{box-sizing:border-box;margin:0;padding:0}
html,body{width:986px;height:1200px;overflow:hidden;background:var(--stage)}
body{position:relative;font-family:"Source Sans 3",sans-serif;color:var(--ink)}
.spread{position:absolute;left:93px;width:800px;height:563px;background:var(--paper);box-shadow:0 6px 18px rgba(0,0,0,.25);overflow:hidden}
.spread--outside{top:24px}
.spread--inside{top:613px}
.panel{position:absolute;top:0;width:266.67px;height:563px;overflow:hidden}
.panel--1{left:0}.panel--2{left:266.67px}.panel--3{left:533.33px}
.abs{position:absolute}
.heading{font-family:"Montserrat",sans-serif;font-weight:800;font-size:10px;line-height:1.15;color:var(--navy);text-transform:uppercase}
.body-text{font-size:8.5px;line-height:1.55;color:var(--ink)}
.title{font-family:"Montserrat",sans-serif;color:var(--teal);line-height:1.15;text-align:right}
.title .name{font-size:15px;display:block}
.title .boxed{display:inline-block;font-size:13px;border:1px solid var(--teal);padding:0 4px;margin-top:2px}
.sky{position:absolute;background:linear-gradient(180deg,#f4fafd 0%,var(--sky-light) 25%,var(--sky-mid) 70%,#a8d3e5 100%)}
.glass{position:absolute;background:linear-gradient(160deg,#dff2fa 0%,#7cc4e0 22%,var(--glass) 50%,#1b6d99 75%,var(--glass-deep) 100%)}
.bullets{list-style:none}
.bullets li{position:relative;padding-left:16px;font-size:8px;line-height:14.5px}
.bullets li::before{content:"";position:absolute;left:1px;top:4px;width:5px;height:5px;border:1px solid var(--glass);border-radius:50%}
.contact{right:34px;text-align:right;font-family:"Montserrat",sans-serif;font-size:8px;line-height:17px;color:var(--navy);font-weight:700}
.contact .row{display:flex;justify-content:flex-end;align-items:center;gap:8px}
.contact .ico{width:12px;height:12px;border:1px solid var(--teal);border-radius:50%;display:inline-flex;align-items:center;justify-content:center}
.contact-name{font-family:"Montserrat",sans-serif;font-weight:700;font-size:8px;color:var(--teal);letter-spacing:.3px}
.hairline{position:absolute;bottom:24px;height:1px;background:var(--rule)}
.cta{font-family:"Montserrat",sans-serif;font-size:10px;color:var(--teal);text-align:right;line-height:1.3}
.cta b{font-style:italic;font-weight:800;color:var(--navy)}
.network-art{position:absolute;left:40px;top:320px;width:185px;height:135px;background:radial-gradient(circle at 50% 50%,#e3ecf6 0%,#f3f7fb 55%,#ffffff 100%)}
.service{position:absolute;left:45px;width:166px;height:67px;background:rgba(255,255,255,.9);border:1px solid #bcd6dc;clip-path:polygon(0 0,100% 0,100% 100%,14px 100%,0 calc(100% - 14px));text-align:center;padding-top:6px}
.service svg{display:block;margin:0 auto 3px}
.service h3{font-size:7px;font-weight:700;color:var(--navy)}
.service p{font-size:5.6px;line-height:1.35;color:var(--navy);padding:0 8px}
.value-box{position:absolute;left:30px;top:118px;width:166px;height:253px;padding:16px 20px}
.value-box .frame{position:absolute;inset:0;z-index:0}
.value-box .content{position:relative;z-index:1}
.value-box p{font-size:7px;line-height:1.75;color:var(--teal);margin-bottom:10px}
.photo{position:absolute}
.donut-label{position:absolute;font-size:6px;line-height:1.2;color:var(--ink)}
</style>
</head>
<body>

<section class="spread spread--outside">
  <div class="panel panel--1">
    <h2 class="heading abs" style="left:26px;top:86px;width:220px">Ihr Partner für nachhaltigen<br>Werterhalt und Rundum-Service</h2>
    <p class="body-text abs" style="left:44px;top:134px;font-size:7.5px">Wir verbinden alle Akteure:</p>
    <ul class="bullets abs" style="left:26px;top:160px">
      <li>Steuerberater,</li><li>Behörden,</li><li>Mieter,</li><li>Bauunternehmen,</li><li>Sanierungsfirmen und</li><li>Versicherungen –</li>
    </ul>
    <p class="body-text abs" style="left:44px;top:266px;font-size:7.5px">für den maximalen Erfolg Ihrer Immobilie.</p>
    <div class="network-art" role="img" aria-label="Illustration: Netzwerk verbundener Symbole für Mieter, Handwerker, Behörden, Versicherung und Eigentümer"></div>
    <div class="hairline" style="left:14px;width:230px"></div>
  </div>

  <div class="panel panel--2">
    <div class="sky" role="img" aria-label="Heller Himmel über einer Glasfassade" style="left:0;top:0;width:267px;height:345px"></div>
    <div class="title abs" style="right:50px;top:148px">
      <span class="name">Haven Crest</span>
      <span class="boxed" style="font-size:11px">Property Stewardship</span>
    </div>
    <p class="cta abs" style="right:34px;top:296px">Kontaktieren Sie uns für<br><b>Ihre individuelle Beratung!</b></p>
    <p class="contact-name abs" style="right:75px;top:405px">JONAS TREWELT</p>
    <div class="contact abs" style="top:428px">
      <div class="row">Info@wohnwerk-jt.de <span class="ico"><svg width="7" height="5" viewBox="0 0 7 5"><rect x=".5" y=".5" width="6" height="4" fill="none" stroke="var(--teal)" stroke-width=".8"/><path d="M.5 .5l3 2 3-2" fill="none" stroke="var(--teal)" stroke-width=".8"/></svg></span></div>
      <div class="row">+49 1573 42 19 605 <span class="ico"><svg width="7" height="7" viewBox="0 0 7 7"><path d="M1.5 .8l1.2 1.4-.6.8a4 4 0 0 0 2 2l.8-.6 1.4 1.2-.8 1a5 5 0 0 1-5-5z" fill="var(--teal)"/></svg></span></div>
      <div class="row">Am Lindenhang 7</div>
      <div class="row">73453 Abtsgmünd <span class="ico"><svg width="6" height="8" viewBox="0 0 6 8"><path d="M3 7.5S.5 4.5.5 3a2.5 2.5 0 0 1 5 0C5.5 4.5 3 7.5 3 7.5z" fill="none" stroke="var(--teal)" stroke-width=".8"/><circle cx="3" cy="3" r=".9" fill="var(--teal)"/></svg></span></div>
    </div>
    <div class="hairline" style="left:26px;width:216px"></div>
  </div>

  <div class="panel panel--3">
    <div class="glass" role="img" aria-label="Glashochhaus aus der Froschperspektive mit Sonnenlicht" style="inset:0"></div>
    <div class="abs" style="right:22px;top:84px;text-align:right;font-family:'Montserrat',sans-serif;color:#fff">
      <span style="display:block;font-size:16px">Haven Crest</span>
      <span style="display:inline-block;font-size:14px;border:1px solid #fff;padding:0 4px;margin-top:3px">Property Stewardship</span>
      <p style="font-size:10px;margin-top:18px;font-style:italic;line-height:1.3">Wenige Objekte –<br><b style="font-weight:800">Intensive Betreuung</b></p>
    </div>
    <p class="abs" style="left:26px;top:502px;font-family:'Montserrat',sans-serif;font-weight:700;font-size:7.5px;color:#fff">JONAS TREWELT</p>
    <div class="abs" style="left:135px;top:484px;border-left:1px solid rgba(255,255,255,.7);padding-left:8px;font-size:6.5px;line-height:1.35;color:#fff">
      Info@wohnwerk-jt.de<br>Mobil: +49 1573 42 19 605<br>Am Lindenhang 7,<br>73453 Abtsgmünd
    </div>
  </div>
</section>

<section class="spread spread--inside">
  <div class="panel panel--1">
    <h2 class="heading abs" style="left:28px;top:50px">Unsere Vision:</h2>
    <p class="body-text abs" style="left:28px;top:80px;width:210px;font-size:7.5px">Durch intensive, ganzheitliche Betreuung und strategisches Life-Cycle-Management sichern wir die nachhaltige Ertragsstärke Ihrer Liegenschaft und steigern ihren Wert.</p>
    <svg class="abs" style="left:64px;top:200px" width="120" height="120" viewBox="0 0 120 120" aria-label="Leistungsbereiche">
      <g fill="none" stroke-width="15" transform="rotate(-150 60 60)">
        <circle cx="60" cy="60" r="44" stroke="#1b4f8a" stroke-dasharray="46 231"/>
        <circle cx="60" cy="60" r="44" stroke="#2d7fbf" stroke-dasharray="46 231" stroke-dashoffset="-46"/>
        <circle cx="60" cy="60" r="44" stroke="#f2a12a" stroke-dasharray="46 231" stroke-dashoffset="-92"/>
        <circle cx="60" cy="60" r="44" stroke="#8c8c8c" stroke-dasharray="46 231" stroke-dashoffset="-138"/>
        <circle cx="60" cy="60" r="44" stroke="#1f5f66" stroke-dasharray="46 231" stroke-dashoffset="-184"/>
        <circle cx="60" cy="60" r="44" stroke="#5a4c9c" stroke-dasharray="47 231" stroke-dashoffset="-230"/>
      </g>
      <text x="60" y="58" text-anchor="middle" font-family="Source Sans 3" font-size="5.5" fill="var(--teal)">Haven Crest</text>
      <text x="60" y="65" text-anchor="middle" font-family="Source Sans 3" font-size="5.5" fill="var(--teal)">Property Stewardship</text>
    </svg>
    <span class="donut-label" style="left:40px;top:194px">Kaufmännische<br>Verwaltung</span>
    <span class="donut-label" style="left:150px;top:194px">Technische Verwaltung<br>&amp; Instandhaltung</span>
    <span class="donut-label" style="left:194px;top:252px">Mieterbetreuung &amp;<br>Kommunikation</span>
    <span class="donut-label" style="left:10px;top:254px">Digitalisierung</span>
    <span class="donut-label" style="left:28px;top:320px">Projektkoordination</span>
    <span class="donut-label" style="left:150px;top:320px">Behörden- &amp;<br>Versicherungsmanagement</span>
    <div class="photo" role="img" aria-label="Hand tippt auf ein digitales Haussymbol mit Checkliste" style="left:0;top:392px;width:267px;height:171px;background:linear-gradient(135deg,#0d2a45 0%,#1f5a80 45%,#5aa1c0 75%,#2b4d5c 100%)"></div>
  </div>

  <div class="panel panel--2">
    <div class="sky" role="img" aria-label="Glasfassade im Gegenlicht" style="inset:0;background:linear-gradient(180deg,#f1f8fc 0%,#cfe8f2 30%,#9fd0e3 65%,#4e9fc4 100%)"></div>
    <h2 class="heading abs" style="left:50px;top:50px;font-size:9px">Unser Leistungsprofil<br><span style="font-weight:400;color:var(--glass)">Für Sie kompakt</span></h2>
    <div class="service" style="top:86px">
      <svg width="20" height="18" viewBox="0 0 20 18"><path d="M2 9L10 2l8 7M4 7.5V16h12V7.5" fill="none" stroke="var(--navy)" stroke-width="1.2"/><circle cx="14" cy="13" r="3" fill="#fff" stroke="var(--navy)"/></svg>
      <h3>Kaufmännische Verwaltung</h3>
      <p>Mietverträge, Mahnwesen, Liquidität, Steuerthemen, Betriebskostenabrechnung, Finanzierungsberatung &amp; -abschluss</p>
    </div>
    <div class="service" style="top:200px">
      <svg width="20" height="18" viewBox="0 0 20 18"><path d="M2 9L10 2l8 7M4 7.5V16h12V7.5" fill="none" stroke="var(--navy)" stroke-width="1.2"/><circle cx="14" cy="13" r="3" fill="#fff" stroke="var(--navy)"/></svg>
      <h3>Technische Verwaltung &amp; Instandhaltung</h3>
      <p>Regelmäßige Objektbegehungen mit Schwerpunkt auf Modernisierung und Sanierung, Fristenüberwachung, Notfallmanagement</p>
    </div>
    <div class="service" style="top:314px">
      <svg width="22" height="18" viewBox="0 0 22 18"><circle cx="7" cy="6" r="3" fill="none" stroke="var(--navy)" stroke-width="1.2"/><path d="M1 16a6 6 0 0 1 12 0M12 10l5-4 5 4v6h-10z" fill="none" stroke="var(--navy)" stroke-width="1.2"/></svg>
      <h3>Mieterbetreuung &amp; Kommunikation</h3>
      <p>Kommunikation, Antragswesen, Versicherungsberatung &amp; -abschluss sowie Schadensmanagement</p>
    </div>
    <div class="service" style="top:428px">
      <svg width="20" height="18" viewBox="0 0 20 18"><path d="M2 9L10 2l8 7M4 7.5V16h12V7.5" fill="none" stroke="var(--navy)" stroke-width="1.2"/><path d="M14 9l3 1v3c0 2-3 3-3 3s-3-1-3-3v-3z" fill="#fff" stroke="var(--navy)"/></svg>
      <h3>Behörden- &amp; Versicherungsmanagement</h3>
      <p>Bonitätsprüfung, Mieterwechsel, Beschwerden, Mieterhöhungen, umfassende Betreuung</p>
    </div>
  </div>

  <div class="panel panel--3">
    <div class="title abs" style="left:30px;top:50px;text-align:left">
      <span class="name" style="font-size:13px">Haven Crest</span>
      <span style="font-size:12px;display:block;margin-top:2px">Property Stewardship</span>
    </div>
    <div class="value-box">
      <svg class="frame" width="166" height="253" viewBox="0 0 166 253" aria-hidden="true"><polygon points="0.5,0.5 165.5,0.5 165.5,252.5 14.5,252.5 0.5,238.5" fill="rgba(255,255,255,.6)" stroke="var(--teal)" stroke-width="1"/></svg>
      <div class="content">
        <h2 class="heading" style="font-size:8.5px;margin-bottom:16px">Unser Mehrwert<br>für Sie!</h2>
        <p>Ganzheitliche Betreuung, bereits vor dem Kauf bis zur nachhaltigen Bewirtschaftung und Modernisierung.</p>
        <p>Vernetzung aller Servicepartner für optimale Wertschöpfung.</p>
        <p>Proaktives Vorgehen bei Förderungen &amp; Energie</p>
        <p>Kontaktieren Sie uns für Ihre individuelle Beratung!</p>
      </div>
    </div>
    <div class="photo" role="img" aria-label="Modernes weißes Mehrfamilienhaus unter blauem Himmel" style="left:0;top:392px;width:267px;height:171px;background:linear-gradient(180deg,#3d8fd6 0%,#8cc3ec 40%,#e9ecef 62%,#9aa39a 85%,#6f8a5c 100%)"></div>
  </div>
</section>

</body>
</html>
```